We need a Glass-Shattering Brochure

We area start up renewable company based in the UK but operate in West Africa. We have a unique blend of local know-how and international exposure to latest solar technology. We pride ourselves in bringing next generation, ground breaking, value for money solar products to Africa.

We are launching a massive campaign to introduce some of the world's best solar product to our high net-worth clients and decision makers. This will be a single brochure of A4 size on 8 pages. Details of the page content is attached.

Also a sample of what we like is attached. The brochure must be clean , fresh, very contemporary and straight to the point - Clear

I have attached a link to some of our installation pictures and some pictures that I think you might need. But feel free to source pictures you think will be appropriate for the intended audience.

You can access some of our paid pictures and installation pictures here https://filedrop-example.net/f/x7KpQm2RtLw9ZvNc4HdYs8BjE

Apologies to everyone. We have just uploaded the brochure content

Target Market(s)

Top company executives

Industry/Entity Type

It Company

Requirements
Must have
• Similar font used in the sample brochure attached. White background. Hint of the green. Please check out our website at www.tolvarpower.co.uk
Nice to have
• Other pictures other than the ones provided

```html
<!DOCTYPE html>
<html lang="en">
<head>
<meta charset="utf-8">
<title>The Tolvar Promise</title>
<link rel="stylesheet" href="https://fonts.googleapis.com/css2?family=Open+Sans:wght@300;400;600&display=swap">
<style>
  :root {
    --ink: #2b2b2b;
    --muted: #666;
    --rule-red: #c8322a;
    --brand-green: #3f9a3a;
    --mint: #e1ebd9;
    --panel-grey: #f1f1f1;
    --panel-edge: #c9c9c9;
    --bar-red: #c9341e;
    --bar-blue: #2f6fe0;
    --line-blue: #4a7fe6;
    --avg-grey: #9a9a9a;
  }
  * { box-sizing: border-box; margin: 0; padding: 0; }
  html, body { width: 848px; height: 1200px; overflow: hidden; background: #fff; }
  body { font-family: "Open Sans", Arial, sans-serif; color: var(--ink); position: relative; }

  .page-title {
    position: absolute; left: 46px; top: 46px;
    font-weight: 300; font-size: 38px; letter-spacing: 0.5px; color: #333;
  }
  .title-rule {
    position: absolute; left: 0; top: 100px; width: 812px; height: 2px; background: var(--rule-red);
  }

  .promise-copy {
    position: absolute; left: 46px; top: 138px; width: 740px;
    font-size: 16.5px; line-height: 20px; font-weight: 400; color: #333;
  }
  .promise-copy p { margin-bottom: 20px; }

  .panel { position: absolute; background: var(--mint); padding: 10px; }
  .panel-inner { width: 100%; height: 100%; background: #fff; border: 1px solid var(--panel-edge); }
  .panel-inner svg { display: block; width: 100%; height: 100%; }
  .panel--overview { left: 43px; top: 510px; width: 513px; height: 430px; }
  .panel--daily { left: 553px; top: 508px; width: 242px; height: 220px; }
  .panel--month { left: 190px; top: 690px; width: 490px; height: 348px; }

  .chart-text { font-family: "Open Sans", Arial, sans-serif; fill: #555; }

  .corner-pattern {
    position: absolute; left: 0; bottom: 0; width: 60px; height: 100px;
    background: linear-gradient(135deg, #bfe3a8 0%, #6cc04a 60%, #3f9a3a 100%);
  }

  .brand {
    position: absolute; left: 0; width: 848px; top: 1086px;
    display: flex; justify-content: center; align-items: center; gap: 10px;
  }
  .brand-dot { width: 34px; height: 34px; border-radius: 50%; background: var(--brand-green); }
  .brand-name { font-size: 30px; font-weight: 600; color: var(--brand-green); letter-spacing: 1px; }
  .site-url {
    position: absolute; left: 0; width: 848px; top: 1152px; text-align: center;
    font-size: 11.5px; color: #444;
  }
</style>
</head>
<body>
  <h1 class="page-title">The Tolvar Promise</h1>
  <div class="title-rule"></div>

  <div class="promise-copy">
    <p>We would replace any defected component with 48hrs of event logging. The minimum expected life span of our solar plant is 11 years<br>
    The performance of the plant will be connected via the internet to our monitoring software. We can also provide the option of capturing this monitoring feature on the client’s phone, or on the flat screen in the office.</p>
    <p>The monitoring software features in real time, energy generated, energy use, state of charge of batteries, general health of the plant<br>
    There are no revolving parts, so it’s absolutely quiet. It will be practical for proximity to residential areas.</p>
    <p>It is very scalable to meet business needs, whether expansion or efficiency projects<br>
    Reduces the needless production of harmful waste like CO2<br>
    Reduce the increase cost of constant fueling<br>
    Prolong the life span of the generators as they will be rarely used<br>
    Its design as Off-Grid mode, so can be deployed to areas that are very remote and reduces the need for constant on-site access, ie islands and villages riverine areas</p>
  </div>

  <!-- Plant overview chart -->
  <div class="panel panel--overview">
    <div class="panel-inner" style="background:var(--panel-grey)">
      <svg viewBox="0 0 493 410" aria-label="Plant overview chart">
        <rect x="8" y="8" width="260" height="22" fill="#fff" stroke="#ccc"/>
        <text class="chart-text" x="16" y="23" font-size="9" font-weight="600">Tolvar Plant 1 : Lagos Overview</text>
        <rect x="8" y="36" width="477" height="366" fill="#fff" stroke="#ccc"/>
        <text class="chart-text" x="215" y="52" font-size="8">from 4/9/2016</text>
        <g class="chart-text" font-size="7">
          <text x="18" y="70">1.3</text><text x="18" y="110">1.2</text><text x="18" y="150">1.1</text>
          <text x="18" y="190">1</text><text x="18" y="230">-1.1</text><text x="18" y="270">-1.2</text>
          <text x="18" y="310">-1.3</text><text x="18" y="350">-1.4</text><text x="18" y="390">-1.5</text>
          <text x="462" y="70">140</text><text x="462" y="140">90</text><text x="462" y="210">60</text>
        </g>
        <line x1="40" y1="62" x2="40" y2="392" stroke="#bbb"/>
        <g fill="var(--bar-red)">
          <rect x="46" y="205" width="14" height="187"/><rect x="66" y="220" width="14" height="172"/>
          <rect x="86" y="230" width="14" height="162"/><rect x="106" y="240" width="14" height="152"/>
          <rect x="126" y="260" width="14" height="132"/><rect x="146" y="270" width="14" height="122"/>
          <rect x="246" y="200" width="14" height="192"/><rect x="266" y="150" width="14" height="242"/>
          <rect x="286" y="170" width="14" height="222"/><rect x="306" y="130" width="14" height="262"/>
          <rect x="326" y="130" width="14" height="262"/><rect x="346" y="140" width="14" height="252"/>
          <rect x="366" y="160" width="14" height="232"/><rect x="386" y="185" width="14" height="207"/>
          <rect x="406" y="175" width="14" height="217"/>
        </g>
        <polyline fill="none" stroke="var(--line-blue)" stroke-width="1.2"
          points="60,148 160,148 240,130 262,180 282,200 302,170 322,195 342,180 362,160 382,170 402,200 430,215"/>
      </svg>
    </div>
  </div>

  <!-- Daily yield chart -->
  <div class="panel panel--daily">
    <div class="panel-inner">
      <svg viewBox="0 0 220 198" aria-label="Daily yield chart">
        <text class="chart-text" x="82" y="14" font-size="7">from 4/21/2016</text>
        <text class="chart-text" font-size="6" transform="translate(12 110) rotate(-90)">Yield (kWh)</text>
        <line x1="24" y1="20" x2="24" y2="150" stroke="#bbb"/>
        <line x1="24" y1="150" x2="205" y2="150" stroke="#bbb"/>
        <polyline fill="none" stroke="var(--line-blue)" stroke-width="1.2"
          points="28,118 45,116 60,118 75,116 90,118 105,114 115,98 125,70 135,40 145,40 155,70 165,90 175,110 185,108 195,124"/>
        <polyline fill="none" stroke="var(--bar-red)" stroke-width="1.2"
          points="28,120 45,122 60,120 75,121 90,120 105,122 120,120 135,121 150,120 165,122 180,120 195,121"/>
        <g class="chart-text" font-size="5">
          <text x="26" y="162">2:00 AM</text><text x="76" y="162">8:00 AM</text>
          <text x="126" y="162">2:00 PM</text><text x="170" y="162">8:00 PM</text>
        </g>
        <rect x="40" y="172" width="140" height="18" fill="#fff" stroke="#ccc"/>
        <line x1="46" y1="181" x2="60" y2="181" stroke="var(--line-blue)"/>
        <text class="chart-text" x="64" y="184" font-size="6">Total yield (kWh) per day</text>
      </svg>
    </div>
  </div>

  <!-- Monthly yield chart -->
  <div class="panel panel--month">
    <div class="panel-inner" style="background:var(--panel-grey)">
      <svg viewBox="0 0 468 326" aria-label="Monthly yield chart">
        <g class="chart-text" font-size="8">
          <rect x="6" y="6" width="38" height="16" fill="#e4e4e4" stroke="#ccc"/><text x="17" y="17">Day</text>
          <rect x="46" y="6" width="42" height="16" fill="#fff" stroke="#ccc"/><text x="53" y="17" fill="#333">Month</text>
          <rect x="90" y="6" width="38" height="16" fill="#e4e4e4" stroke="#ccc"/><text x="100" y="17">Year</text>
          <rect x="130" y="6" width="38" height="16" fill="#e4e4e4" stroke="#ccc"/><text x="139" y="17">Total</text>
        </g>
        <rect x="6" y="24" width="456" height="270" fill="#fff" stroke="#ccc"/>
        <text class="chart-text" x="182" y="40" font-size="7">Tolvar Plant 1 Lagos: June 2016</text>
        <text class="chart-text" font-size="6" transform="translate(24 170) rotate(-90)">Total yield (kWh)</text>
        <g class="chart-text" font-size="6">
          <text x="36" y="243">0</text><text x="36" y="207">2</text><text x="36" y="171">4</text>
          <text x="36" y="135">6</text><text x="36" y="99">8</text><text x="36" y="63">10</text>
        </g>
        <line x1="50" y1="55" x2="50" y2="240" stroke="#bbb"/>
        <line x1="50" y1="240" x2="450" y2="240" stroke="#bbb"/>
        <g fill="var(--bar-blue)">
          <rect x="55" y="81.6" width="9" height="158.4"/><rect x="68" y="162.6" width="9" height="77.4"/>
          <rect x="81" y="142.8" width="9" height="97.2"/><rect x="94" y="96" width="9" height="144"/>
          <rect x="107" y="128.4" width="9" height="111.6"/><rect x="120" y="88.8" width="9" height="151.2"/>
          <rect x="133" y="164.4" width="9" height="75.6"/><rect x="146" y="79.8" width="9" height="160.2"/>
          <rect x="159" y="157.2" width="9" height="82.8"/><rect x="172" y="90.6" width="9" height="149.4"/>
          <rect x="185" y="69" width="9" height="171"/><rect x="198" y="130.2" width="9" height="109.8"/>
          <rect x="211" y="128.4" width="9" height="111.6"/><rect x="224" y="139.2" width="9" height="100.8"/>
          <rect x="237" y="162.6" width="9" height="77.4"/><rect x="250" y="144.6" width="9" height="95.4"/>
          <rect x="263" y="112.2" width="9" height="127.8"/><rect x="276" y="81.6" width="9" height="158.4"/>
          <rect x="289" y="85.2" width="9" height="154.8"/><rect x="302" y="128.4" width="9" height="111.6"/>
          <rect x="315" y="123" width="9" height="117"/>
        </g>
        <line x1="50" y1="130.2" x2="450" y2="130.2" stroke="var(--avg-grey)" stroke-width="1.5"/>
        <g class="chart-text" font-size="5.5">
          <text transform="translate(61 262) rotate(-90)">6/2016</text>
          <text transform="translate(113 262) rotate(-90)">6/4/2016</text>
          <text transform="translate(165 262) rotate(-90)">6/8/2016</text>
          <text transform="translate(217 262) rotate(-90)">6/12/2016</text>
          <text transform="translate(269 262) rotate(-90)">6/16/2016</text>
          <text transform="translate(321 262) rotate(-90)">6/20/2016</text>
          <text transform="translate(373 262) rotate(-90)">6/24/2016</text>
          <text transform="translate(425 262) rotate(-90)">6/30/2016</text>
        </g>
        <rect x="130" y="270" width="230" height="16" fill="#fff" stroke="#ccc"/>
        <rect x="138" y="274" width="9" height="8" fill="var(--bar-blue)"/>
        <text class="chart-text" x="151" y="281" font-size="6.5">Total yield</text>
        <line x1="240" y1="278" x2="256" y2="278" stroke="var(--avg-grey)" stroke-width="1.5"/>
        <text class="chart-text" x="260" y="281" font-size="6.5">Average yield expectations</text>
        <rect x="8" y="306" width="7" height="7" fill="#fff" stroke="#888"/>
        <text class="chart-text" x="18" y="313" font-size="6.5">Display the prediction</text>
        <rect x="226" y="302" width="40" height="14" fill="#fff" stroke="#bbb"/>
        <text class="chart-text" x="236" y="312" font-size="7">Jun</text>
        <rect x="272" y="302" width="44" height="14" fill="#fff" stroke="#bbb"/>
        <text class="chart-text" x="280" y="312" font-size="7">2016</text>
      </svg>
    </div>
  </div>

  <div class="corner-pattern" role="img" aria-label="Decorative green square tile pattern"></div>

  <div class="brand">
    <span class="brand-dot"></span>
    <span class="brand-name">TOLVAR POWER</span>
  </div>
  <div class="site-url">www.tolvarpower.co.uk</div>
</body>
</html>
```